Clean Stationary Design For Print Shop

I need a clean stationary set that properly represents a local print and copy shop to make it look amazing. It should do the following:
- Compliment the color scheme of the logo.
- Be clean and sharp.
- Be colorful but but balanced.

This is what I need designed:
- Business Card
- Letter Head
- Envelop

Target Market(s)

Local customers and businesses, including hospitals and schools.

Industry/Entity Type

Digital Printing

Requirements
Must have
• Clean business card with logo on front and full color back with faded logo on it and social icons with @hollowmeadowsco beside each one (Facebook & Instagram).

```html
<!DOCTYPE html>
<html lang="en">
<head>
<meta charset="utf-8">
<title>Hollow Meadows — Stationery Set</title>
<link href="https://fonts.googleapis.com/css2?family=Open+Sans:wght@400;600;700&display=swap" rel="stylesheet">
<style>
:root{
  --red:#ff2d4a;
  --ink:#231f20;
  --text:#2b2b2b;
  --paper:#ffffff;
  --backdrop:#e6e6e6;
  --muted:#8a8a8a;
}
*{box-sizing:border-box;margin:0;padding:0}
html,body{width:1200px;height:882px;overflow:hidden}
body{background:var(--backdrop);font-family:"Open Sans",Arial,sans-serif;color:var(--text);position:relative}
.sheet{position:absolute;background:var(--paper);overflow:hidden}
.brand{position:absolute;white-space:nowrap}
.brand-mark{display:inline-block;background:var(--red);vertical-align:middle}
.brand-name{font-weight:600;color:var(--ink);vertical-align:middle}
.brand-tag{display:block;font-weight:700;color:var(--muted);letter-spacing:.03em}
.contact{position:absolute;line-height:1.45;white-space:nowrap}
.contact .row{display:flex;align-items:flex-start;gap:4px}
.contact svg{flex:none;margin-top:1px}
.strip{position:absolute;left:0;right:0;bottom:0}
.strip-pattern{position:absolute;left:0;bottom:0;height:100%;background:linear-gradient(90deg,#6e6e6e,#3a3a3a 40%,var(--ink) 70%)}
.web-tab{position:absolute;right:0;bottom:0;background:var(--red);color:#fff;font-weight:600;display:flex;align-items:center;justify-content:flex-end;clip-path:polygon(12% 0,100% 0,100% 100%,0 100%)}
.social{position:absolute;display:flex;align-items:center}
.social .dot{border-radius:50%;background:var(--red);display:inline-block}
.person-name{position:absolute;color:var(--red);font-weight:700}
.person-role{position:absolute}

/* business card front */
.card-front{left:106px;top:148px;width:222px;height:127px}
.card-front .brand{left:12px;top:11px}
.card-front .brand-mark{width:9px;height:13px;margin-right:3px}
.card-front .brand-name{font-size:9px}
.card-front .brand-tag{font-size:2.6px;margin-left:12px;margin-top:-2px}
.card-front .person-name{left:12px;top:76px;font-size:9.5px}
.card-front .person-role{left:12px;top:89px;font-size:6.5px}
.card-front .contact{left:122px;top:50px;font-size:5.6px}
.card-front .gap{height:9px}
.card-front .strip{height:7px}
.card-front .strip-pattern{width:140px}
.card-front .strip-dark{position:absolute;left:130px;right:0;bottom:0;height:7px;background:var(--ink)}
.card-front .web-tab{width:86px;height:14px;font-size:5px;padding-right:6px}

/* business card back */
.card-back{left:353px;top:148px;width:221px;height:127px;background:var(--ink)}
.card-back .pattern{position:absolute;left:0;top:0;bottom:0;width:135px;background:linear-gradient(90deg,#8a8a8a,#4a4a4a 55%,var(--ink))}
.card-back .brand{left:148px;top:84px;text-align:center}
.card-back .brand-mark{display:block;width:20px;height:28px;margin:0 auto 6px}
.card-back .brand-name{color:#fff;font-size:8.5px}
.card-back .brand-tag{font-size:2.6px;color:#b9b9b9}

/* DL envelope */
.envelope-dl{left:106px;top:308px;width:475px;height:219px}
.envelope-dl .brand{left:17px;top:13px}
.envelope-dl .brand-mark{display:block;width:34px;height:40px;margin:0 0 6px 24px}
.envelope-dl .brand-name{font-size:11.5px}
.envelope-dl .brand-tag{font-size:3.2px}
.envelope-dl .contact{left:12px;top:190px;font-size:6px}
.envelope-dl .social{left:188px;top:190px;font-size:6.5px;gap:4px}
.envelope-dl .social .dot{width:12px;height:12px}
.envelope-dl .strip{height:11px}
.envelope-dl .strip-pattern{width:200px}
.envelope-dl .strip-dark{position:absolute;left:190px;width:125px;bottom:0;height:11px;background:var(--ink)}
.envelope-dl .web-tab{width:166px;height:23px;font-size:10px;padding-right:9px}

/* C4 envelope */
.envelope-c4{left:106px;top:565px;width:475px;height:218px}
.envelope-c4 .flap{position:absolute;left:0;top:0;width:475px;height:56px}
.envelope-c4 .brand{left:0;right:0;top:17px;text-align:center}
.envelope-c4 .brand-name{color:#fff;font-size:15px;font-weight:700}
.envelope-c4 .social{left:19px;top:192px;font-size:6.5px;gap:4px}
.envelope-c4 .social .dot{width:12px;height:12px}

/* letterhead */
.letterhead{left:603px;top:75px;width:501px;height:708px}
.letterhead .brand{left:38px;top:28px}
.letterhead .brand-mark{display:block;width:41px;height:48px;margin:0 0 6px 29px}
.letterhead .brand-name{font-size:12.5px}
.letterhead .brand-tag{font-size:3.4px}
.letterhead .contact{left:348px;top:25px;font-size:8.8px;line-height:1.4}
.letterhead .contact .gap{height:8px}
.letter-body{position:absolute;left:38px;top:183px;width:436px;font-size:9.6px;line-height:15.7px}
.letter-body p{margin-bottom:15.7px}
.letter-body .salutation{margin-bottom:15.7px}
.signature{position:absolute;left:26px;top:530px;width:122px;height:38px;background:linear-gradient(90deg,rgba(60,60,60,.12),rgba(60,60,60,.05));border-radius:19px}
.letterhead .person-name{left:37px;top:576px;font-size:12px}
.letterhead .person-role{left:38px;top:592px;font-size:8.6px}
.letterhead .social{left:38px;top:667px;font-size:8.8px;gap:5px}
.letterhead .social .dot{width:17px;height:17px}
.letterhead .strip{height:12px}
.letterhead .strip-pattern{width:210px}
.letterhead .strip-dark{position:absolute;left:200px;width:115px;bottom:0;height:12px;background:var(--ink)}
.letterhead .web-tab{width:194px;height:26px;font-size:11.5px;padding-right:15px}
</style>
</head>
<body>

<!-- Business card front -->
<section class="sheet card-front">
  <div class="brand"><span class="brand-mark"></span><span class="brand-name">Hollow Meadows</span><span class="brand-tag">PRINT · COPY · DESIGN</span></div>
  <div class="person-name">Mara Ellison</div>
  <div class="person-role">Owner</div>
  <div class="contact">
    <div class="row"><svg width="5" height="7" viewBox="0 0 10 14"><path d="M5 0a5 5 0 0 1 5 5c0 4-5 9-5 9S0 9 0 5a5 5 0 0 1 5-5z" fill="#ff2d4a"/><circle cx="5" cy="5" r="2" fill="#fff"/></svg><span>27 Mill Lane, Suite 4<br>P.O Box 5810, 40213 USA</span></div>
    <div class="gap"></div>
    <div class="row"><svg width="5" height="6" viewBox="0 0 10 10"><circle cx="5" cy="5" r="4" fill="none" stroke="#ff2d4a" stroke-width="1.4"/></svg><span>555-014-2290</span></div>
    <div class="row"><svg width="5" height="6" viewBox="0 0 10 10"><circle cx="5" cy="5" r="4" fill="none" stroke="#ff2d4a" stroke-width="1.2"/><path d="M1 5h8M5 1v8" stroke="#ff2d4a" stroke-width="1"/></svg><span>hello@hollowmeadows.co<br>www.hollowmeadows.co</span></div>
  </div>
  <div class="strip">
    <div class="strip-pattern" role="img" aria-label="Repeating monogram pattern band"></div>
    <div class="strip-dark"></div>
    <div class="web-tab">www.hollowmeadows.co</div>
  </div>
</section>

<!-- Business card back -->
<section class="sheet card-back">
  <div class="pattern" role="img" aria-label="Repeating monogram pattern fading to black"></div>
  <div class="brand"><span class="brand-mark"></span><span class="brand-name">Hollow Meadows</span><span class="brand-tag">PRINT · COPY · DESIGN</span></div>
</section>

<!-- DL envelope -->
<section class="sheet envelope-dl">
  <div class="brand"><span class="brand-mark"></span><span class="brand-name">Hollow Meadows</span><span class="brand-tag">PRINT · COPY · DESIGN</span></div>
  <div class="contact"><div class="row"><svg width="7" height="10" viewBox="0 0 10 14"><path d="M5 0a5 5 0 0 1 5 5c0 4-5 9-5 9S0 9 0 5a5 5 0 0 1 5-5z" fill="#ff2d4a"/><circle cx="5" cy="5" r="2" fill="#fff"/></svg><span>27 Mill Lane, Suite 4, P.O Box 5810, 40213 USA</span></div></div>
  <div class="social"><span class="dot"></span><span class="dot"></span><span class="dot"></span><span>@hollowmeadowsco</span></div>
  <div class="strip">
    <div class="strip-pattern" role="img" aria-label="Repeating monogram pattern band"></div>
    <div class="strip-dark"></div>
    <div class="web-tab">www.hollowmeadows.co</div>
  </div>
</section>

<!-- C4 envelope -->
<section class="sheet envelope-c4">
  <svg class="flap" viewBox="0 0 475 56"><path d="M0 0H475L463 35Q455 56 432 56H43Q20 56 12 35Z" fill="#ff2d4a"/></svg>
  <div class="brand"><span class="brand-name">Hollow Meadows</span></div>
  <div class="social"><span class="dot"></span><span class="dot"></span><span class="dot"></span><span>@hollowmeadowsco</span></div>
</section>

<!-- Letterhead -->
<section class="sheet letterhead">
  <div class="brand"><span class="brand-mark"></span><span class="brand-name">Hollow Meadows</span><span class="brand-tag">PRINT · COPY · DESIGN</span></div>
  <div class="contact">
    <div class="row"><svg width="8" height="11" viewBox="0 0 10 14"><path d="M5 0a5 5 0 0 1 5 5c0 4-5 9-5 9S0 9 0 5a5 5 0 0 1 5-5z" fill="#ff2d4a"/><circle cx="5" cy="5" r="2" fill="#fff"/></svg><span>27 Mill Lane, Suite 4<br>P.O Box 5810, 40213 USA</span></div>
    <div class="gap"></div>
    <div class="row"><svg width="8" height="9" viewBox="0 0 10 10"><circle cx="5" cy="5" r="4" fill="none" stroke="#ff2d4a" stroke-width="1.4"/></svg><span>555-014-2290</span></div>
    <div class="row"><svg width="8" height="9" viewBox="0 0 10 10"><circle cx="5" cy="5" r="4" fill="none" stroke="#ff2d4a" stroke-width="1.2"/><path d="M1 5h8M5 1v8" stroke="#ff2d4a" stroke-width="1"/></svg><span>hello@hollowmeadows.co<br>www.hollowmeadows.co</span></div>
  </div>
  <div class="letter-body">
    <p class="salutation">Dear Sir,</p>
    <p>Dolor sit amet, consectetuer adipiscing elit, sed diam nonummy nibh euismod tincidunt ut laoreet dolore magna aliquam erat volutpat. Ut wisi enim ad minim veniam, quis nostrud exerci tation ullamcorper suscipit lobortis nisl ut aliquip ex ea commodo consequat. Duis autem vel eum iriure dolor in hendrerit in vulputate velit esse molestie consequat, vel illum dolore eu feugiat nulla facilisis at vero eros et accumsan et iusto odio dignissim qui blandit praesent luptatum zzril delenit augue duis dolore te feugait nulla facilisi.</p>
    <p>Lorem ipsum dolor sit amet, cons ectetuer adipiscing elit, sed diam nonummy nibh euismod tincidunt ut laoreet dolore magna aliquam erat volutpat. Ut wisi enim ad minim veniam, quis nostrud exerci tation ullamcorper suscipit lobortis nisl ut aliquip ex ea commodo consequat.</p>
    <p>Lorem ipsum dolor sit amet, consectetuer adipiscing elit, sed diam nonummy nibh euismod tincidunt ut laoreet dolore magna aliquam erat volutpat. Ut wisi enim ad minim veniam, quis nostrud exerci tation ullamcorper suscipit lobortis nisl ut aliquip ex ea commodo consequat. Duis</p>
  </div>
  <div class="signature" role="img" aria-label="Handwritten signature of the owner"></div>
  <div class="person-name">Mara Ellison</div>
  <div class="person-role">Owner</div>
  <div class="social"><span class="dot"></span><span class="dot"></span><span class="dot"></span><span>@hollowmeadowsco</span></div>
  <div class="strip">
    <div class="strip-pattern" role="img" aria-label="Repeating monogram pattern band"></div>
    <div class="strip-dark"></div>
    <div class="web-tab">www.hollowmeadows.co</div>
  </div>
</section>

</body>
</html>
```